Reverse Mortgage Postcard Design - SIZE: 8.5" x 6"

FRONT OF CARD:

HEADLINE:
Reverse Mortgage Program
FHA/ HUD Insured Loan Eliminates Mortgage Payments Forever

You’ve worked hard for your retirement years. You owe it to yourself to find out what the FHA/ HUD Insured Home Equity Conversion Mortgage can do for you. Thousands of Homeowners Nationwide are taking advantage of this program.

If you are 62+ years of age, and live in your own home, you may qualify for this program that allows you to remain in your home while eliminate mortgage payments - FOREVER.

Call Marisol Trent Today for your FREE Information Kit and Private Concierge Consultation
(415) 730-4461

Discover in 2 minutes if a Home Equity Conversion Mortgage is right for you.

INCLUDE IN FRONT OF CARD: COMPANY LOGO & PICTURE OF SENIOR COUPLE

BACK OF CARD - INCLUDE: BRIGHTWAY HOME LOANS LOGO, HEADSHOT OF MARISOL TRENT, FHA LOGO, HUD LOGO, office address:

(BRIGHTWAY HOME LOAN LOGO +)
2715 Orchard Vale Road Suite 300
San Rafael, CA 94817
(415) 730-4461

TESTIMONIAL:

“We had questions if a Reverse Mortgage was right for us. Marisol from Brightway Home Loans was friendly and helped us every step of the way. We couldn’t be happier.” – R. Halvorsen

Benefits Available:
:
 Equity Cash Withdrawal
 Eliminate Mortgage Payments Forever
 Retain Homeownership
 FHA/HUD Insured program

HEADSHOT OF MARISOL TRENT +

Call Marisol Trent
Senior Mortgage Advisor
(415) 730-4461
NMLS # 587430 CA BRE # 2049361

- For Your FREE Information Kit -

FINE PRINT DISCLOSURES (smaller type):

Brightway Home Loans, dba Curtis Bellamy NMLS #615284. 18657 Silver Birch, Dana Point CA 92714. Homeowner remains responsible for paying property taxes, insurance and home maintenance. These materials are not from or approved by HUD.

* ADD FHA AND HUD LOGO *
** Please leave room for mailing indicia and required address space for Post Office **

Target Market(s)

Senior citizens 62+.

Industry/Entity Type

Loan

Requirements
Must have
• I am asking them to trust me with reviewing their finances in relation to their home. It's a very serious proposition, and there are many concerns about security of their financial future..the main thing is, I need to make them pick up the phone and call me. Once I engage with these customers I can gain rapport and provide them excellent service. So if you have any ideas - copy wise - as to how to get them to pick up the phone and call, by all means let me know!!

```html
<!DOCTYPE html>
<html lang="en">
<head>
<meta charset="utf-8">
<title>Brightway Home Loans – Reverse Mortgage Postcard</title>
<link href="https://fonts.googleapis.com/css2?family=Montserrat:wght@400;600;700;800&family=Open+Sans:ital,wght@0,400;0,600;0,700;1,400&display=swap" rel="stylesheet">
<style>
  :root{
    --navy:#12306b;
    --blue:#1f5fae;
    --sky:#2d8ad6;
    --orange:#f0821e;
    --orange-dark:#d8660d;
    --ink:#2b2f38;
    --paper:#ffffff;
    --backdrop:#d9dbe0;
    --muted:#6b7280;
  }
  *{box-sizing:border-box;margin:0;padding:0}
  html,body{width:849px;height:1200px;overflow:hidden;background:var(--backdrop)}
  body{font-family:"Open Sans",Arial,sans-serif;color:var(--ink);position:relative}
  .card{position:absolute;left:44px;width:760px;height:536px;background:var(--paper);overflow:hidden;box-shadow:0 4px 14px rgba(0,0,0,.18)}
  .card--front{top:40px}
  .card--back{top:624px}
  .brand{display:flex;align-items:center;gap:8px;font-family:"Montserrat",Arial,sans-serif;font-weight:800;color:var(--navy);font-size:17px;letter-spacing:.5px}
  .brand__mark{width:14px;height:14px;background:var(--orange)}

  /* front */
  .front__brand{position:absolute;left:28px;top:24px}
  .front__copy{position:absolute;left:28px;top:70px;width:330px}
  .headline{font-family:"Montserrat",Arial,sans-serif;color:var(--navy);line-height:1}
  .headline__top{font-size:27px;font-weight:700;letter-spacing:.5px}
  .headline__main{font-size:52px;font-weight:800;letter-spacing:1px}
  .subhead{font-family:"Montserrat",Arial,sans-serif;font-weight:700;margin-top:8px;line-height:1.2}
  .subhead__line{font-size:14px;color:var(--navy)}
  .subhead__accent{font-size:19px;color:var(--orange)}
  .front__body{margin-top:16px;font-size:11.5px;line-height:1.5}
  .front__body p+p{margin-top:10px}
  .front__photo{position:absolute;right:0;top:0;width:400px;height:420px}
  .discover{position:absolute;left:380px;top:232px;width:150px;height:150px;border-radius:50%;background:var(--orange);color:#fff;text-align:center;display:flex;flex-direction:column;justify-content:center;padding:14px;border:4px solid #fff}
  .discover__big{font-family:"Montserrat",Arial,sans-serif;font-weight:800;font-size:21px;line-height:1.05}
  .discover__small{font-size:10px;line-height:1.3;margin-top:6px}
  .front__band{position:absolute;left:0;bottom:0;width:100%;height:96px;background:var(--navy);display:flex;align-items:center;justify-content:space-between;padding:0 28px;color:#fff}
  .band__call{font-family:"Montserrat",Arial,sans-serif;font-weight:700;font-size:16px;line-height:1.35;width:480px}
  .band__call .hl{color:var(--orange)}
  .band__visit{text-align:right}
  .band__visit-label{font-family:"Montserrat",Arial,sans-serif;font-weight:800;color:var(--orange);font-size:30px}
  .band__url{font-size:10.5px}

  /* back */
  .back__brand{position:absolute;left:34px;top:24px}
  .back__col{position:absolute;left:34px;top:70px;width:380px}
  .tab{display:inline-block;background:var(--blue);color:#fff;font-family:"Montserrat",Arial,sans-serif;font-weight:700;font-size:13px;padding:5px 16px 5px 12px;text-transform:uppercase}
  .tab--title{text-transform:none}
  .quote{font-size:10.5px;line-height:1.5;margin:8px 0 4px;font-style:italic}
  .quote__by{text-align:right;font-size:10.5px;font-weight:700;color:var(--navy);margin-bottom:12px}
  .benefits{list-style:none;margin:8px 0 14px}
  .benefits li{display:flex;align-items:center;gap:8px;font-size:12px;font-weight:600;margin:4px 0}
  .advisor{display:flex;gap:14px;background:var(--blue);color:#fff;padding:10px;border-radius:4px;align-items:center}
  .advisor__photo{width:86px;height:86px;border:3px solid #fff;background:linear-gradient(160deg,#c9a58a,#7c5a45)}
  .advisor__name{font-family:"Montserrat",Arial,sans-serif;font-weight:700;font-size:15px}
  .advisor__role{font-size:11px}
  .advisor__phone{font-family:"Montserrat",Arial,sans-serif;font-weight:800;font-size:24px;margin:2px 0}
  .advisor__lic{font-size:9px}
  .back__footer{position:absolute;left:34px;bottom:18px;width:380px;display:flex;justify-content:space-between;align-items:flex-end}
  .address{font-size:9.5px;line-height:1.4;color:var(--navy)}
  .fineprint{font-size:6.5px;line-height:1.3;color:var(--muted);margin-top:4px;width:300px}
  .badges{display:flex;gap:6px}
  .badge{width:30px;height:30px;border:2px solid var(--navy);border-radius:4px}
  .badge--round{border-radius:50%}
</style>
</head>
<body>

<section class="card card--front">
  <div class="front__photo" role="img" aria-label="Smiling senior couple embracing outdoors" style="background:linear-gradient(135deg,#b9cfa4 0%,#8aa678 45%,#d8c3ad 100%)"></div>
  <svg class="front__swoosh" width="760" height="536" viewBox="0 0 760 536" style="position:absolute;left:0;top:0">
    <path d="M360 0 C330 140 350 300 420 440 L392 440 C320 300 300 140 330 0 Z" fill="var(--sky)"/>
    <path d="M375 0 C350 140 368 300 440 440 L425 440 C355 300 338 140 362 0 Z" fill="var(--orange)"/>
    <path d="M0 420 C260 400 520 410 760 380 L760 440 L0 440 Z" fill="var(--blue)"/>
  </svg>
  <div class="brand front__brand"><span class="brand__mark"></span>BRIGHTWAY HOME LOANS</div>
  <div class="front__copy">
    <h1 class="headline">
      <div class="headline__top">REVERSE MORTGAGE</div>
      <div class="headline__main">PROGRAM</div>
    </h1>
    <div class="subhead">
      <div class="subhead__line">FHA/ HUD INSURED LOAN ELIMINATES</div>
      <div class="subhead__accent">MORTGAGE PAYMENTS FOREVER</div>
    </div>
    <div class="front__body">
      <p>You've worked hard for your retirement years. You owe it to yourself to find out what the FHA/ HUD Insured Home Equity Conversion Mortgage can do for you. Thousands of Homeowners Nationwide are taking advantage of this program.</p>
      <p>If you are 62+ years of age, and live in your own home, you may qualify for this program that allows you to remain in your home while eliminating mortgage payments - FOREVER.</p>
    </div>
  </div>
  <div class="discover">
    <div class="discover__big">Discover in 2 minutes</div>
    <div class="discover__small">if a Home Equity Conversion Mortgage is right for you.</div>
  </div>
  <div class="front__band">
    <div class="band__call">Call Marisol Trent Today for your <span class="hl">FREE Information Kit</span> and <span class="hl">Private Concierge Consultation</span> (415) 730-4461</div>
    <div class="band__visit">
      <div class="band__visit-label">visit us</div>
      <div class="band__url">www.brightwayreverseloans.com</div>
    </div>
  </div>
</section>

<section class="card card--back">
  <svg width="760" height="536" viewBox="0 0 760 536" style="position:absolute;left:0;top:0">
    <path d="M0 0 L18 0 C8 180 8 360 18 536 L0 536 Z" fill="var(--blue)"/>
    <path d="M18 0 L24 0 C14 180 14 360 24 536 L18 536 Z" fill="var(--orange)"/>
    <path d="M440 0 C470 40 600 70 760 60 L760 0 Z" fill="var(--blue)"/>
    <path d="M440 0 C480 52 610 84 760 74 L760 62 C600 72 472 42 452 0 Z" fill="var(--orange)"/>
  </svg>
  <div class="brand back__brand"><span class="brand__mark"></span>BRIGHTWAY HOME LOANS</div>
  <div class="back__col">
    <div class="tab">Testimonial</div>
    <p class="quote">"I read about Marisol in the Sunday Bay Ledger. I was impressed with her from the start and still am. She follows through, she cares, she is honest. She has a great attitude and explains all the details. I would you still find anyone more worthy of your business."</p>
    <div class="quote__by">- Elena P. Mill Valley</div>
    <div class="tab tab--title">Benefits Available</div>
    <ul class="benefits">
      <li><svg width="14" height="14" viewBox="0 0 14 14"><path d="M2 7 L6 11 L12 3" stroke="var(--orange)" stroke-width="2.5" fill="none"/></svg>Equity Cash Withdrawal</li>
      <li><svg width="14" height="14" viewBox="0 0 14 14"><path d="M2 7 L6 11 L12 3" stroke="var(--orange)" stroke-width="2.5" fill="none"/></svg>Eliminate Mortgage Payments Forever</li>
      <li><svg width="14" height="14" viewBox="0 0 14 14"><path d="M2 7 L6 11 L12 3" stroke="var(--orange)" stroke-width="2.5" fill="none"/></svg>Retain Homeownership</li>
      <li><svg width="14" height="14" viewBox="0 0 14 14"><path d="M2 7 L6 11 L12 3" stroke="var(--orange)" stroke-width="2.5" fill="none"/></svg>FHA/HUD Insured program</li>
    </ul>
    <div class="advisor">
      <div class="advisor__photo" role="img" aria-label="Headshot of advisor Marisol Trent"></div>
      <div>
        <div class="advisor__name">Call Marisol Trent</div>
        <div class="advisor__role">Senior Mortgage Advisor</div>
        <div class="advisor__phone">(415) 730-4461</div>
        <div class="advisor__lic">NMLS # 587430 CA BRE # 2049361</div>
      </div>
    </div>
    <p class="fineprint">Brightway Home Loans, dba Curtis Bellamy NMLS #615284. 18657 Silver Birch, Dana Point CA 92714. Homeowner remains responsible for paying property taxes, insurance and home maintenance. These materials are not from or approved by HUD.</p>
  </div>
  <div class="back__footer">
    <div class="address">www.brightwayreverseloans.com<br>2715 Orchard Vale Road Suite 300, San Rafael, CA 94817</div>
    <div class="badges"><span class="badge"></span><span class="badge badge--round"></span></div>
  </div>
</section>

</body>
</html>
```